Larkfield Clinic Marketing Flyer

We are a new medical practice in the community and need a flyer to send to other medical offices to inform of our services. We just completed our logo with PixelGuild and would like to incorporate that plus our marketing content into the flyer. Our medical practice has 2 divisions: (1)Mental Health/Psychiatry and (2) Migraine and Neurospasticity Management. Please see website for content and provider photos at www.LarkfieldCare.example

Target Market(s)

Other Healthcare Professionals in the Community

Industry/Entity Type

Medical

Requirements
Must have
• Photos of all 5 healthcare providers, phone number, address, logo

```html
<!DOCTYPE html>
<html lang="en">
<head>
<meta charset="utf-8">
<title>Larkfield Clinic Flyer</title>
<link href="https://fonts.googleapis.com/css2?family=Poppins:wght@400;500;600;700&display=swap" rel="stylesheet">
<style>
:root{
  --teal:#0f8a78;
  --lime:#8dc63f;
  --grey:#555a5e;
  --paper:#ffffff;
  --bg:#ffffff;
  --photo-a:#b9cfe6;
  --photo-b:#e8eef5;
}
*{margin:0;padding:0;box-sizing:border-box}
html,body{width:1200px;height:1200px;overflow:hidden;background:var(--bg);font-family:'Poppins',sans-serif}
.flyer{position:absolute;left:200px;top:95px;width:800px;height:1035px;background:var(--paper);overflow:hidden}
.abs{position:absolute;white-space:nowrap}
.provider-photo{position:absolute;left:450px;top:130px;width:350px;height:870px;
  background:radial-gradient(ellipse 60% 55% at 60% 60%,var(--photo-a) 0%,var(--photo-b) 60%,rgba(255,255,255,0) 100%)}
.brand{left:40px;top:50px;display:flex;align-items:center;gap:14px}
.brand-dot{width:52px;height:52px;border-radius:50%;background:var(--teal)}
.brand-name{font-size:30px;font-weight:500;color:var(--teal)}
.website{right:22px;top:24px;font-size:23px;color:var(--teal)}
.phone{right:22px;top:60px;display:flex;align-items:center;gap:10px;font-size:37px;font-weight:600;color:var(--lime)}
.headline-small{left:40px;top:190px;font-size:38px;font-weight:500;color:var(--teal)}
.headline-big{left:40px;top:228px;font-size:66px;font-weight:700;color:var(--lime);line-height:1.2}
.tag-box{left:41px;top:329px;width:270px;height:62px;background:var(--teal);color:#fff;font-size:37px;font-weight:500;display:flex;align-items:center;justify-content:center}
.services{left:38px;top:402px;font-size:21.5px;color:var(--grey);line-height:27px}
.services b{font-weight:600}
.portal-title{left:38px;top:514px;font-size:37px;font-weight:700;color:var(--teal)}
.portal-intro{left:39px;top:562px;font-size:22px;color:var(--grey);line-height:29px}
.portal-intro b{font-weight:600}
.feature{left:38px;display:flex;align-items:center;gap:14px;font-size:31px;font-weight:500;color:var(--teal)}
.feature svg{width:36px;height:36px}
.loc-box{left:302px;top:914px;width:197px;height:35px;background:var(--teal);color:#fff;font-size:21px;display:flex;align-items:center;justify-content:center}
.loc-name{left:0;width:800px;text-align:center;top:952px;font-size:22px;font-weight:700;color:var(--lime)}
.loc-address{left:107px;top:980px;font-size:22px;color:var(--teal)}
</style>
</head>
<body>
<main class="flyer">
  <div class="provider-photo" role="img" aria-label="Smiling healthcare provider in blue scrubs and cap holding a stethoscope"></div>

  <div class="abs brand"><span class="brand-dot"></span><span class="brand-name">Larkfield Clinic</span></div>

  <div class="abs website">www.<b>LarkfieldCare</b>.example</div>
  <div class="abs phone">
    <svg width="40" height="40" viewBox="0 0 40 40"><circle cx="20" cy="20" r="20" fill="var(--lime)"/><path d="M14 10c1.5-1 2.5 0 3.5 2l1 2.5c.5 1.2 0 2-1 2.8-.8.6-.6 1.5 0 2.6 1 1.6 2.2 2.9 3.8 3.8 1 .6 1.9.7 2.5-.1.8-1 1.6-1.5 2.8-1l2.5 1.1c2 .9 2.9 2 2 3.5-1.5 2.5-4 3.3-7 2-5-2.2-9-6.2-11-11-1.2-3-.5-5.6 1.9-8.2z" fill="#fff"/></svg>
    (208)555-0146
  </div>

  <div class="abs headline-small">Helping Bodies</div>
  <div class="abs headline-big">Helping Minds</div>
  <div class="abs tag-box">Helping You</div>

  <div class="abs services"><b>Mental Health</b> and Psychiatry Services<br>Migraine and Neurospasticity Intervention</div>

  <div class="abs portal-title">Join us on the Portal!</div>
  <div class="abs portal-intro"><b>We know</b> your days are busy!<br>Use our Patient Portal for:</div>

  <div class="abs feature" style="top:658px">
    <svg viewBox="0 0 36 36"><path d="M18 4C10 4 4 9.5 4 16.5c0 3.5 1.5 6.5 4 8.8L6.5 31l6.5-3c1.5.5 3.2.8 5 .8 8 0 14-5.5 14-12.3S26 4 18 4z" fill="none" stroke="var(--teal)" stroke-width="2.2"/><circle cx="12" cy="16.5" r="1.7" fill="var(--teal)"/><circle cx="18" cy="16.5" r="1.7" fill="var(--teal)"/><circle cx="24" cy="16.5" r="1.7" fill="var(--teal)"/></svg>
    Online Messaging</div>
  <div class="abs feature" style="top:721px">
    <svg viewBox="0 0 36 36"><rect x="8" y="6" width="18" height="24" fill="none" stroke="var(--teal)" stroke-width="2"/><path d="M12 13h10M12 18h10M12 23h6" stroke="var(--teal)" stroke-width="2"/><path d="M22 28l8-10" stroke="var(--teal)" stroke-width="2.4"/></svg>
    Prescription Renewal</div>
  <div class="abs feature" style="top:787px">
    <svg viewBox="0 0 36 36"><rect x="4" y="11" width="19" height="14" rx="2" fill="var(--teal)"/><path d="M24 16l8-4v12l-8-4z" fill="var(--teal)"/></svg>
    Virtual Visits</div>
  <div class="abs feature" style="top:842px">
    <svg viewBox="0 0 36 36"><rect x="4" y="11" width="28" height="15" fill="none" stroke="var(--teal)" stroke-width="2"/><rect x="8" y="14" width="20" height="9" fill="none" stroke="var(--teal)" stroke-width="1.2"/><circle cx="18" cy="18.5" r="3" fill="none" stroke="var(--teal)" stroke-width="1.6"/></svg>
    Pay Your Bill</div>

  <div class="abs loc-box">Locations</div>
  <div class="abs loc-name">Larkfield Clinic</div>
  <div class="abs loc-address">215 W. Alderbrook, Suite A&nbsp; Maple Falls, ID 83000</div>
</main>
</body>
</html>
```